Business Advisory Firm Business Card

A clean, very upscale looking business card. Not crowded.

Please include logo (attached) and:

Danielle R. Kastrup
Four Ashgrove Court
New York, NY 10087
tel: (917) 555-3140
fax: (646) 555-2973
email: dkastrup@silvermerepartners.example
website: www.silvermerepartners.example

Target Market(s)

Business clients. Often real estate development firms, other advisory firms or growing companies that need assistance. I would like a card that looks impressive and confident.

Industry/Entity Type

Business

Colors

Designer to choose colors to be used in the design.

Requirements
Must have
• Impressive and confident. Please include logo.
Should not have
• nothing flashy...

```html
<!DOCTYPE html>
<html lang="en">
<head>
<meta charset="utf-8">
<title>Silvermere Advisory Partners – Business Card</title>
<link rel="stylesheet" href="https://fonts.googleapis.com/css2?family=Arimo:wght@400;700&display=swap">
<style>
  :root {
    --page-bg: #e9eced;
    --card-white: #ffffff;
    --wave-grey: #d3d9db;
    --card-charcoal: #2d383d;
    --ink-dark: #2d3a3e;
    --accent-orange: #f25a1b;
    --accent-lime: #b9d63a;
    --text-light: #ffffff;
  }
  * { margin: 0; padding: 0; box-sizing: border-box; }
  html, body {
    width: 1200px;
    height: 1000px;
    overflow: hidden;
    background: var(--page-bg);
    font-family: "Arimo", Arial, sans-serif;
  }
  .business-card {
    position: absolute;
    left: 57px;
    top: 182px;
    width: 1086px;
    height: 634px;
    background: var(--card-white);
    overflow: hidden;
  }
  .card-waves {
    position: absolute;
    inset: 0;
    width: 100%;
    height: 100%;
  }
  .wave-band { fill: var(--wave-grey); }
  .wave-base { fill: var(--card-charcoal); }
  .brand-mark {
    position: absolute;
    left: 196px;
    top: 74px;
    width: 104px;
    height: 104px;
    background: var(--accent-lime);
  }
  .brand-name {
    position: absolute;
    left: 426px;
    top: 92px;
    color: var(--ink-dark);
    font-weight: 400;
    font-size: 46px;
    line-height: 45px;
    font-variant: small-caps;
    letter-spacing: 0.5px;
  }
  .holder-name {
    position: absolute;
    left: 183px;
    top: 402px;
    color: var(--accent-orange);
    font-weight: 700;
    font-size: 45px;
    line-height: 54px;
  }
  .contact-list {
    position: absolute;
    left: 426px;
    top: 465px;
    list-style: none;
    color: var(--text-light);
  }
  .contact-list li {
    font-size: 24px;
    line-height: 31px;
    white-space: nowrap;
  }
  .contact-list li.contact-small {
    font-size: 21px;
    line-height: 29px;
  }
</style>
</head>
<body>
  <main class="business-card">
    <svg class="card-waves" viewBox="0 0 1086 634" preserveAspectRatio="none" aria-hidden="true">
      <path class="wave-band" d="M0 236 C180 310 330 370 470 355 C640 335 760 225 900 232 C990 236 1050 270 1086 300 L1086 634 L0 634 Z"/>
      <path class="wave-base" d="M0 273 C170 330 300 370 450 365 C620 358 760 262 920 265 C1000 268 1050 300 1086 330 L1086 634 L0 634 Z"/>
    </svg>

    <div class="brand-mark" aria-hidden="true"></div>
    <h1 class="brand-name">Silvermere<br>Advisory<br>Partners, Inc.</h1>

    <h2 class="holder-name">Danielle R. Kastrup</h2>
    <ul class="contact-list">
      <li>Four Ashgrove Court, New York, NY 10087</li>
      <li>tel: (917) 555-3140 • fax: (646) 555-2973</li>
      <li class="contact-small">email: dkastrup@silvermerepartners.example</li>
      <li class="contact-small">website: www.silvermerepartners.example</li>
    </ul>
  </main>
</body>
</html>
```